International professional tennis coach needs a book cover design

This is my 2nd published book, the first one was a #1 on the best seller. I'm looking for a world class book cover design for this new book. The name of my first book was 5 Baseline Habits to Unlock Your Rally Rhythm, located on Brimlow.com

The title of the new book:

Title: The Craft of Steady Rallies
Subtitle: Building a Tactical Margin by Way of Opponent Insight

I'm uploading our new CRAFT OF STEADY logo that I'd like for you to use as the centerpiece of the book design along with a 21st century design feel that incorporates what the book topic is below::

--> This book is about building competitive intelligence by using tennis data analytics to develop and expand a player's strategic advantage for match play. <--

The colors we would like to use are Blue, Yellow, and Green. These shades of these colors should be bold! (You will see the bold color examples of blues, yellows, and greens that I'm talking about in the logos that are attached here, especially the colors for my Tennis GridRally App logo.

I will upload the Tennis GridRally logo which should go somewhere on the back cover design (small size maybe in the bottom corner).

This book is revolutionary to the standard way of teaching tennis, it is based on a decade of recording and gathering tennis data analytics and then we created on-court practice games to develop better decision making in players for the competitive edge.

My websites are www.elevatedrillzone.com and www.craftofsteadyrallies.com

```html
<!DOCTYPE html>
<html lang="en">
<head>
<meta charset="utf-8">
<title>The Craft of Steady Rallies — Book Cover</title>
<link href="https://fonts.googleapis.com/css2?family=Bebas+Neue&family=Montserrat:wght@500;600&display=swap" rel="stylesheet">
<style>
  :root {
    --stage: #282828;
    --paper: #ffffff;
    --ink: #404040;
    --ink-soft: #2b2b2b;
    --court-blue: #1f76bb;
    --ball-yellow: #f8c116;
  }
  * { margin: 0; padding: 0; box-sizing: border-box; }
  html, body {
    width: 1200px;
    height: 1200px;
    overflow: hidden;
    background: var(--stage);
  }
  .cover {
    position: absolute;
    left: 237px;
    top: 53px;
    width: 728px;
    height: 1092px;
    background: var(--paper);
    overflow: hidden;
  }
  .subtitle {
    position: absolute;
    top: 46px;
    left: 0;
    width: 100%;
    text-align: center;
    font-family: "Montserrat", sans-serif;
    font-weight: 500;
    font-size: 27px;
    line-height: 43px;
    letter-spacing: 0.035em;
    color: var(--ink-soft);
  }
  .title-art {
    position: absolute;
    left: 0;
    top: 0;
    width: 728px;
    height: 720px;
  }
  .title-line {
    font-family: "Bebas Neue", sans-serif;
    font-weight: 400;
  }
  .title-lead { fill: var(--ink); }
  .title-main { fill: var(--court-blue); }
  .title-end  { fill: var(--ball-yellow); }
  .brand-mark {
    position: absolute;
    left: 0;
    top: 720px;
    width: 100%;
    height: 270px;
    display: flex;
    align-items: center;
    justify-content: center;
    gap: 22px;
  }
  .brand-dot {
    width: 58px;
    height: 58px;
    border-radius: 50%;
    background: var(--ball-yellow);
  }
  .brand-name {
    font-family: "Montserrat", sans-serif;
    font-weight: 600;
    font-size: 44px;
    letter-spacing: 0.06em;
    color: var(--court-blue);
  }
  .author-band {
    position: absolute;
    left: 0;
    bottom: 0;
    width: 100%;
    height: 82px;
    background: var(--court-blue);
    display: flex;
    align-items: center;
    justify-content: center;
  }
  .author-name {
    font-family: "Montserrat", sans-serif;
    font-weight: 500;
    font-size: 44px;
    letter-spacing: 0.12em;
    color: var(--paper);
  }
</style>
</head>
<body>
  <main class="cover">
    <p class="subtitle">Building a Tactical Margin<br>by Way of Opponent Insight</p>
    <h1>
      <svg class="title-art" viewBox="0 0 728 720" role="img" aria-label="The Craft of Steady Rallies">
        <text class="title-line title-lead" x="364" y="259" text-anchor="middle" font-size="144" textLength="500" lengthAdjust="spacingAndGlyphs">THE CRAFT OF</text>
        <text class="title-line title-main" x="364" y="455" text-anchor="middle" font-size="256" textLength="626" lengthAdjust="spacingAndGlyphs">STEADY</text>
        <text class="title-line title-end" x="364" y="690" text-anchor="middle" font-size="300" textLength="628" lengthAdjust="spacingAndGlyphs">RALLIES</text>
      </svg>
    </h1>
    <div class="brand-mark">
      <span class="brand-dot"></span>
      <span class="brand-name">CRAFT OF STEADY</span>
    </div>
    <footer class="author-band">
      <span class="author-name">DORIAN KELVALE</span>
    </footer>
  </main>
</body>
</html>
```